Anzeigengestaltung für Immobilienmakler
Zielgruppe
Immobilienmakler, Zielgruppe: Private (selten gewerbliche) Immobilienverkäufer/-käufer, Immobilienvermietung
Aufgabenstellung
Unser Logo soll Berücksichtigung finden, gerne auch wir als Personen. Design angelehnt an Logo und Schriftbild (siehe Anhang) und Website.
Headline: Ihre Immobilienvermittler für die Bodenseeregion.
Vorteile darstellen:
- Lokale Marktkenntnis: Wir kennen die Besonderheiten des regionalen Immobilienmarkts
-Persönliche Betreuung: Bei uns stehen Sie im Mittelpunkt
- Starkes Netzwerk: Profitieren Sie von unseren guten Beziehungen
- Kompletter Service: Von der ersten Beratung über die Erstellung des Exposés bis hin zur Vertragsabwicklung – wir bieten Ihnen alles aus einer Hand.
- Ausgebildet: GWA zertifizierte Immobilienmakler und Verbandszugehörigkeit
Kontaktdaten angeben:Festnetz/ Mobilfunknummer und Homepage, Ort: Salem
Das ganze in einem klaren und wertigen Design.
Die Anzeige soll sich im Text anpassen lassen und bitte in verschiedenen Formaten ausgeworfen werden (verschiedene Größen, ggf. kleinere Größen mit weniger textlichem Inhalt)

```html
<!DOCTYPE html>
<html lang="de">
<head>
<meta charset="utf-8">
<title>Kaltenbach Makler – Anzeige</title>
<link rel="stylesheet" href="https://fonts.googleapis.com/css2?family=Outfit:wght@300;400;600;700&display=swap">
<style>
  :root {
    --navy: #364a6e;
    --ink: #2f4368;
    --muted: #7c88a8;
    --white: #ffffff;
    --illus-a: #dfe3ec;
    --illus-b: #6f7f9f;
  }
  html, body {
    margin: 0;
    padding: 0;
    width: 1200px;
    height: 1200px;
    overflow: hidden;
    background: var(--white);
  }
  .ad {
    position: relative;
    width: 1200px;
    height: 1200px;
    font-family: "Outfit", sans-serif;
    color: var(--ink);
    overflow: hidden;
  }
  .hero {
    position: absolute;
    left: 0; top: 0;
    width: 1200px;
    height: 442px;
    background: var(--navy);
  }
  .brand {
    position: absolute;
    left: 0; top: 66px;
    width: 1200px;
    margin: 0;
    text-align: center;
    font-weight: 400;
    font-size: 24px;
    line-height: 1;
    letter-spacing: 0.5px;
    color: var(--white);
  }
  .headline {
    position: absolute;
    left: 62px; top: 141px;
    margin: 0;
    font-weight: 700;
    font-size: 89px;
    line-height: 1;
    letter-spacing: 0.6px;
    color: var(--white);
    white-space: nowrap;
  }
  .headline-sub {
    position: absolute;
    left: 106px; top: 228px;
    margin: 0;
    font-weight: 300;
    font-size: 91px;
    line-height: 1;
    letter-spacing: 1.2px;
    color: var(--muted);
    white-space: nowrap;
  }
  .intro {
    position: absolute;
    left: 109px; top: 331px;
    margin: 0;
    font-weight: 400;
    font-size: 20.5px;
    letter-spacing: 0.9px;
    color: var(--muted);
    white-space: nowrap;
  }
  .benefit { position: absolute; }
  .benefit h2 {
    margin: 0 0 10px;
    font-weight: 600;
    font-size: 37px;
    line-height: 1;
    letter-spacing: 0.5px;
    color: var(--ink);
    white-space: nowrap;
  }
  .benefit p {
    margin: 0;
    font-weight: 400;
    font-size: 22.5px;
    line-height: 24px;
    letter-spacing: 0.7px;
    color: var(--ink);
    white-space: nowrap;
  }
  .benefit-local    { left: 109px; top: 488px; }
  .benefit-personal { left: 551px; top: 488px; }
  .benefit-network  { left: 110px; top: 603px; }
  .benefit-trained  { left: 561px; top: 603px; }
  .benefit-service  { left: 109px; top: 720px; }
  .benefit-service h2 { margin-bottom: 15px; }
  .contact {
    position: absolute;
    left: 111px; top: 975px;
    margin: 0;
    font-style: normal;
    font-size: 16.5px;
    line-height: 20px;
    letter-spacing: 0.4px;
    color: var(--ink);
  }
  .house-illustration {
    position: absolute;
    left: 612px; top: 758px;
    width: 588px; height: 438px;
    background: linear-gradient(160deg, var(--illus-a) 0%, #b4bdd0 55%, var(--illus-b) 100%);
  }
  .ground-line {
    position: absolute;
    left: 612px; top: 1195px;
    width: 588px; height: 1.5px;
    background: var(--ink);
  }
</style>
</head>
<body>
  <main class="ad">
    <header class="hero">
      <p class="brand">Kaltenbach Makler</p>
      <h1 class="headline">Ihre Immobilienvermittler</h1>
      <p class="headline-sub">für die Bodenseeregion.</p>
      <p class="intro">Wir bieten umfassende Beratung und Betreuung&nbsp; für Kauf, Verkauf und Vermietung von Immobilien.</p>
    </header>

    <section class="benefit benefit-local">
      <h2>Lokale Marktkenntnis:</h2>
      <p>Wir kennen die Besonderheiten des<br>regionalen Immobilienmarkts</p>
    </section>
    <section class="benefit benefit-personal">
      <h2>Persönliche Betreuung:</h2>
      <p>Bei uns stehen Sie im Mittelpunkt</p>
    </section>
    <section class="benefit benefit-network">
      <h2>Starkes Netzwerk:</h2>
      <p>Profitieren Sie von unseren<br>guten Beziehungen</p>
    </section>
    <section class="benefit benefit-trained">
      <h2>Ausgebildet:</h2>
      <p>GWA zertifizierte Immobilienmakler<br>und Verbandszugehörigkeit</p>
    </section>
    <section class="benefit benefit-service">
      <h2>Kompletter Service:</h2>
      <p>Von der ersten Beratung über die Erstellung<br>des Exposés bis hin zur Vertragsabwicklung –<br>wir bieten Ihnen alles aus einer Hand.</p>
    </section>

    <address class="contact">
      Telefon: +49 (0)7553 4471209<br>
      Mobil: +49 (0)157 62018834<br>
      E-Mail: kontakt@kaltenbach-makler.de<br>
      Adresse: Am Weiherweg 7, 88682 Salem<br>
      Website: www.kaltenbach-makler.de
    </address>

    <div class="house-illustration" role="img" aria-label="Linienillustration eines modernen Einfamilienhauses mit Satteldach, großer Giebelverglasung, Baum und Wolken"></div>
    <div class="ground-line"></div>
  </main>
</body>
</html>
```